Webdesign für industrielle Produktion von Suppen, Saucen, Bouillons und Konzentraten
Zielgruppe
Industrielle Produktion von Suppen, Saucen, Bouillons und Konzentraten
Aufgabenstellung
Aufmachung nicht zu modern, eher klassisch Understatement

```html
<!DOCTYPE html>
<html lang="de">
<head>
<meta charset="utf-8">
<title>Kornhaus Foodservice</title>
<link rel="stylesheet" href="https://fonts.googleapis.com/css2?family=Open+Sans:wght@300;400;600;700;800&display=swap">
<style>
:root{
  --red:#e10a0a;
  --red-deep:#a30000;
  --red-card:#a50505;
  --red-footer:#b00000;
  --nav:#4d4d4d;
  --text:#333;
  --muted:#888;
  --border:#d9b7a8;
  --review:#e7d1d1;
  --white:#fff;
}
*{box-sizing:border-box;margin:0;padding:0}
html,body{width:1200px;height:4757px;overflow:hidden}
body{font-family:"Open Sans",Arial,sans-serif;color:var(--text);background:var(--white);position:relative}
.abs{position:absolute}
section,header,footer{position:relative;width:1200px}

/* header */
.topbar{height:79px}
.brand{left:107px;top:10px;display:flex;align-items:center;gap:8px}
.brand-mark{width:16px;height:16px;border-radius:50%;background:var(--red)}
.brand-name{font-size:26px;font-weight:700;color:var(--red);line-height:1}
.brand-sub{font-size:11px;font-weight:700;color:var(--red);display:block;margin-top:2px;padding-left:24px}
.phone{left:310px;top:24px;display:flex;align-items:center;gap:12px;font-size:20px;font-weight:600;color:#222}
.account{left:838px;top:28px;font-size:15px;color:#555}
.tools{left:975px;top:24px;display:flex;gap:18px}
.cart{position:relative}
.cart-badge{position:absolute;right:-6px;top:-5px;width:12px;height:12px;border-radius:50%;background:var(--red);color:#fff;font-size:8px;text-align:center;line-height:12px}
.mainnav{height:36px;background:var(--nav);display:flex;justify-content:space-between;padding:0 100px 0 101px;align-items:center}
.mainnav a{color:#fff;text-decoration:none;font-size:15.5px}

/* hero */
.hero{height:439px;background:linear-gradient(100deg,#2b1f18 0%,#5a3e2a 35%,#8a6040 55%,#3a2a20 100%)}
.hero-title{left:107px;top:266px;font-size:42px;font-weight:800;color:#fff;letter-spacing:.5px}
.hero-sub{left:107px;top:331px;font-size:20px;color:#fff;line-height:24px}
.btn-shop{left:107px;top:299px;width:163px;height:53px;background:var(--red);color:#fff;font-size:17px;display:flex;align-items:center;justify-content:center;border-radius:4px}

/* intro */
.intro{height:1034px}
.intro-title{left:107px;top:112px;font-size:43px;font-weight:300;line-height:51px;color:#444}
.intro-title b{font-weight:700}
.feature-icon{width:93px;height:93px;border-radius:50%;border:1.5px solid #c9a096;background:#fbf3f1;display:flex;align-items:center;justify-content:center}
.feature-text{width:340px;font-size:11.5px;line-height:24px;color:#555}
.quality-card{left:539px;top:310px;width:465px;height:613px;background:var(--red-card);border-radius:18px;color:#fff;text-align:center;padding:198px 55px 0}
.quality-card h2{font-size:27px;font-weight:700;line-height:34px;margin-bottom:26px}
.quality-card p{font-size:15.5px;line-height:19.5px;margin-bottom:19px}
.soup-bowl{left:578px;top:46px;width:388px;height:388px;border-radius:50%;background:radial-gradient(circle at 50% 50%,#e8cf6a 0%,#d9b843 55%,#f2f2f2 60%,#d8d8d8 70%,#ffffff 72%)}
.sauce-bowls{left:950px;top:720px;width:250px;height:267px;border-radius:50% 0 0 50%;background:radial-gradient(circle at 40% 40%,#f0c040,#c0402a 55%,#f4efe6 80%,rgba(255,255,255,0) 100%)}

/* categories */
.categories{height:194px;display:flex}
.category{width:600px;height:194px;display:flex;align-items:center;justify-content:center;font-size:50px;font-weight:800;color:#fff;letter-spacing:1px}
.cat-soups{background:linear-gradient(90deg,#6d6b62,#8c8a80 50%,#5f5c55)}
.cat-sauces{background:linear-gradient(90deg,#6e1414,#8a1d1d 50%,#5c0f0f)}

/* products */
.products{height:714px}
.pill{left:50%;transform:translateX(-50%);height:70px;padding:0 18px;background:var(--red);border-radius:14px;box-shadow:0 0 0 3px #fff,0 0 0 5px var(--red);color:#fff;font-size:29px;font-weight:700;display:flex;align-items:center;white-space:nowrap}
.product-card{width:281px;height:352px;border:1.5px solid var(--border);border-radius:14px;text-align:center}
.product-shot{left:70px;top:-20px;width:140px;height:142px;border-radius:8px;background:linear-gradient(180deg,#c9c9c9 0%,#b3322d 30%,#d8b070 65%,#b8b8b8 100%)}
.product-name{position:absolute;top:147px;width:100%;font-size:15.5px;color:#333}
.product-price{position:absolute;top:170px;width:100%;font-size:21px;font-weight:700;color:#c7502a}
.product-note{position:absolute;top:198px;width:100%;font-size:11.5px;color:var(--muted)}
.qty{position:absolute;top:245px;left:44px;width:192px;height:35px;display:flex;justify-content:space-between}
.qty span{height:35px;border:1px solid #e3e3e3;display:flex;align-items:center;justify-content:center;font-size:15px;box-shadow:0 1px 3px rgba(0,0,0,.12)}
.qty .step{width:42px}
.qty .count{width:88px;border:none;box-shadow:none}
.add-cart{position:absolute;top:292px;left:44px;width:192px;height:36px;background:var(--red);border-radius:4px;color:#fff;font-size:12px;display:flex;align-items:center;justify-content:center;gap:14px}
.slider-nav{left:517px;display:flex;gap:18px}
.slider-nav span{width:74px;height:52px;border-radius:22px;display:flex;align-items:center;justify-content:center}
.prev{background:#dcdcdc}
.next{background:var(--red)}

/* natural band */
.natural{height:502px}
.band{left:231px;top:0;width:969px;height:435px;background:var(--red-deep);border-radius:70px 0 0 0}
.band-photo{left:59px;top:24px;width:355px;height:424px;border-radius:90px 0 0 0;background:linear-gradient(180deg,#dfe7e4 0%,#c8d4cf 40%,#d77a3a 62%,#c93c3c 80%,#e9dede 100%)}
.badge{left:323px;top:37px;width:148px;height:148px;border-radius:50%;background:#5cb335;color:#fff;text-align:center;font-weight:800;font-size:18px;line-height:20px;display:flex;flex-direction:column;justify-content:center}
.band-text{left:591px;top:98px;width:510px;color:#fff;font-size:15.5px;line-height:24px}
.band-text p+p{margin-top:24px}

/* reviews */
.reviews{height:591px;background:var(--review);text-align:center}
.reviews h2{position:absolute;top:58px;width:100%;font-size:40px;font-weight:700;color:var(--red);letter-spacing:.5px}
.reviews .lead{position:absolute;top:106px;width:100%;font-size:20px;color:#8a4a3a}
.review-product{left:554px;top:168px;width:92px;height:92px;border-radius:50%;background:radial-gradient(circle,#d9c4b0 0%,#a87a5d 70%)}
.quote-mark{left:117px;top:212px;font-size:460px;line-height:340px;font-weight:800;color:#fff;font-family:Georgia,serif}
.review-text{position:absolute;top:280px;left:270px;width:660px;font-size:16px;line-height:24px;color:#444}
.review-meta{position:absolute;width:100%;font-size:16px;color:#444}
.review-meta b{font-weight:700;color:#333}
.dots{left:577px;top:528px;display:flex;gap:12px}
.dots span{width:18px;height:18px;border-radius:50%;border:2px solid var(--red)}
.dots span:first-child{background:var(--red)}

/* footer */
.site-footer{height:526px}
.footer-brand{left:107px;top:48px;width:207px;height:105px;border:3px solid var(--red);border-radius:18px;display:flex;flex-direction:column;align-items:center;justify-content:center;gap:2px}
.footer-brand .brand-name{font-size:34px}
.footer-brand .brand-sub{padding:0;font-size:14px}
.news-title{left:559px;top:55px;font-size:20px;font-weight:700;color:#222}
.news-form{left:559px;top:98px;width:536px;height:53px;display:flex}
.news-input{flex:1;background:#efefef;font-size:13px;color:#444;display:flex;align-items:center;padding-left:27px}
.news-btn{width:164px;background:var(--red);color:#fff;font-size:16px;display:flex;align-items:center;justify-content:center}
.foot-col{top:246px;font-size:12px;line-height:18.5px;color:#444}
.foot-col h3{font-size:14.5px;font-weight:700;color:#222;margin-bottom:24px;letter-spacing:.3px}
.foot-col .u{text-decoration:underline;display:inline-block;width:64px}
.to-top{left:1075px;top:250px}
.legal{left:0;top:473px;width:1200px;height:53px;background:var(--red-footer);color:#fff;font-size:12px;display:flex;align-items:center;justify-content:space-between;padding:0 104px 0 107px}
.social{display:flex;gap:22px}
.social span{width:22px;height:22px;border-radius:50%;background:#fff}
</style>
</head>
<body>

<header>
  <div class="topbar">
    <div class="abs brand"><span class="brand-mark"></span><div><span class="brand-name">kornhaus</span><span class="brand-sub">Foodservice</span></div></div>
    <div class="abs phone">
      <svg width="28" height="28" viewBox="0 0 24 24" fill="#222"><path d="M6.6 10.8c1.4 2.8 3.8 5.1 6.6 6.6l2.2-2.2c.3-.3.7-.4 1-.2 1.1.4 2.3.6 3.6.6.6 0 1 .4 1 1V20c0 .6-.4 1-1 1C10.6 21 3 13.4 3 4c0-.6.4-1 1-1h3.5c.6 0 1 .4 1 1 0 1.3.2 2.5.6 3.6.1.3 0 .7-.2 1z"/></svg>
      +49-(0)-2104-88320
    </div>
    <div class="abs account">kornhaus-profi®</div>
    <div class="abs tools">
      <svg width="26" height="26" viewBox="0 0 24 24" fill="none" stroke="#222" stroke-width="1.8"><circle cx="12" cy="12" r="10"/><circle cx="12" cy="10" r="3.5"/><path d="M5.5 19c1.5-3 4-4 6.5-4s5 1 6.5 4"/></svg>
      <svg width="26" height="26" viewBox="0 0 24 24" fill="none" stroke="#222" stroke-width="2"><circle cx="10" cy="10" r="7"/><path d="M15 15l6 6"/></svg>
      <span class="cart"><svg width="26" height="26" viewBox="0 0 24 24" fill="none" stroke="#222" stroke-width="1.8"><path d="M2 3h3l2.5 12h11L21 7H6"/><circle cx="9" cy="19.5" r="1.5"/><circle cx="17" cy="19.5" r="1.5"/></svg><span class="cart-badge">0</span></span>
    </div>
  </div>
  <nav class="mainnav">
    <a href="#">Startseite</a><a href="#">Shop</a><a href="#">GV-Produkte</a><a href="#">Gastronomie-Produkte</a><a href="#">Neuigkeiten</a><a href="#">Wir über uns</a><a href="#">Downloads</a><a href="#">Kontakt</a>
  </nav>
</header>

<section class="hero" role="img" aria-label="Kochtopf mit gelber Suppe auf einem Gasherd in einer Küche">
  <h1 class="abs hero-title" style="top:152px">KORNHAUS FOODSERVICE</h1>
  <p class="abs hero-sub" style="top:220px">für vorbildlichen Gastronomie-<br>und GV-Service</p>
  <span class="abs btn-shop">Zum Shop</span>
</section>

<section class="intro">
  <h2 class="abs intro-title">An der Suppe &amp; an der<br>Sauce <b>wird der<br>Koch gemessen!</b></h2>

  <div class="abs feature-icon" style="left:107px;top:351px">
    <svg width="46" height="46" viewBox="0 0 24 24" fill="none" stroke="#a05a50" stroke-width="1.2"><path d="M4 20c6-2 12-8 14-16-8 2-14 8-14 16z"/><path d="M4 20L14 10"/></svg>
  </div>
  <p class="abs feature-text" style="left:107px;top:467px">Die Güte der Endprodukte wird durch die Verwendung nur bester Rohstoffe gewährleistet. Wir vertreiben unsere Topqualität unter dem Motto „First Class“. Seit mehr als 75 Jahren liefern wir immer pünktlich ohne Qualitätsreklamationen. Die Aus- lieferung erfolgt nach Auftragseingang am folgenden Tag.</p>

  <div class="abs feature-icon" style="left:107px;top:659px">
    <svg width="46" height="46" viewBox="0 0 24 24" fill="none" stroke="#a05a50" stroke-width="1.2"><path d="M12 20s-8-5-8-11a4 4 0 0 1 8-1 4 4 0 0 1 8 1c0 6-8 11-8 11z"/></svg>
  </div>
  <p class="abs feature-text" style="left:107px;top:775px">Die Rückverfolgung der einzelnen Produktionschargen ist sichergestellt. Alle Kornhaus Produkte haben eine garantierte Restlaufzeit von mindestens 30 Monaten.</p>

  <div class="abs quality-card">
    <h2>Genial &amp; edler als<br>Trockenprodukte</h2>
    <p>Kornhaus steht für vorbildliche und gepflegte Gastlichkeit in der gehobenen Gastronomie, im guten GV-Service und im Top-Party-Service</p>
    <p>Sie können mit Kornhaus Spezialitäten allen Ansprüchen Ihrer Gäste nach einer kleinen Mahlzeit gerecht werden. Schneller, besser und wirtschaftlicher geht es nicht! Wir garantieren qualitative Beständigkeit und Unverfälschtheit. Das sieht man und das schmeckt man!</p>
  </div>
  <div class="abs soup-bowl" role="img" aria-label="Teller mit Brokkoli-Käsesuppe"></div>
  <div class="abs sauce-bowls" role="img" aria-label="Schälchen mit verschiedenen Saucen und Kräutern"></div>
</section>

<section class="categories">
  <div class="category cat-soups" role="img" aria-label="Verschiedene Suppen in Schalen">SUPPEN</div>
  <div class="category cat-sauces" role="img" aria-label="Tomaten auf dunkelrotem Grund">SAUCEN</div>
</section>

<section class="products">
  <h2 class="abs pill" style="top:57px">Top-Produkte</h2>
  <div class="abs product-card" style="left:107px;top:194px">
    <div class="abs product-shot" role="img" aria-label="Konservendose Kartoffelsuppe"></div>
    <div class="product-name">Kartoffelsuppen-Terrine 1/4</div><div class="product-price">1,82 €</div><div class="product-note">inkl. MwSt. zzgl. Versandkosten</div>
    <div class="qty"><span class="step">-</span><span class="count">3</span><span class="step">+</span></div>
    <div class="add-cart"><svg width="16" height="16" viewBox="0 0 24 24" fill="none" stroke="#fff" stroke-width="2"><path d="M2 3h3l2.5 12h11L21 7H6"/><circle cx="9" cy="19.5" r="1.5"/><circle cx="17" cy="19.5" r="1.5"/></svg>In den Warenkorb</div>
  </div>
  <div class="abs product-card" style="left:461px;top:194px">
    <div class="abs product-shot" role="img" aria-label="Konservendose Hühnersuppe" style="background:linear-gradient(180deg,#d0d0d0,#c43a33 25%,#f2efe8 45%,#e07a3a 80%,#c0c0c0)"></div>
    <div class="product-name">Kartoffelsuppen-Terrine 1/4</div><div class="product-price">1,82 €</div><div class="product-note">inkl. MwSt. zzgl. Versandkosten</div>
    <div class="qty"><span class="step">-</span><span class="count">1</span><span class="step">+</span></div>
    <div class="add-cart"><svg width="16" height="16" viewBox="0 0 24 24" fill="none" stroke="#fff" stroke-width="2"><path d="M2 3h3l2.5 12h11L21 7H6"/><circle cx="9" cy="19.5" r="1.5"/><circle cx="17" cy="19.5" r="1.5"/></svg>In den Warenkorb</div>
  </div>
  <div class="abs product-card" style="left:814px;top:194px">
    <div class="abs product-shot" role="img" aria-label="Konservendose Hühnersuppe dunkel" style="background:linear-gradient(180deg,#b0b0b0,#8c1212 25%,#5a1010 60%,#3a0c0c 90%)"></div>
    <div class="product-name">Kartoffelsuppen-Terrine 1/4</div><div class="product-price">1,82 €</div><div class="product-note">inkl. MwSt. zzgl. Versandkosten</div>
    <div class="qty"><span class="step">-</span><span class="count">1</span><span class="step">+</span></div>
    <div class="add-cart"><svg width="16" height="16" viewBox="0 0 24 24" fill="none" stroke="#fff" stroke-width="2"><path d="M2 3h3l2.5 12h11L21 7H6"/><circle cx="9" cy="19.5" r="1.5"/><circle cx="17" cy="19.5" r="1.5"/></svg>In den Warenkorb</div>
  </div>
  <div class="abs slider-nav" style="top:593px">
    <span class="prev"><svg width="30" height="14" viewBox="0 0 30 14" fill="none" stroke="#999" stroke-width="1.6"><path d="M29 7H2M8 1L2 7l6 6"/></svg></span>
    <span class="next"><svg width="30" height="14" viewBox="0 0 30 14" fill="none" stroke="#fff" stroke-width="1.6"><path d="M1 7h27M22 1l6 6-6 6"/></svg></span>
  </div>
</section>

<section class="natural">
  <div class="abs band"></div>
  <div class="abs band-photo" role="img" aria-label="Schale Gemüsesuppe auf rot-weiß kariertem Tischtuch im Garten"></div>
  <div class="abs badge"><span>100%</span><span>NATURAL</span></div>
  <div class="abs band-text">
    <p>Steigende Löhne und wachsende Ansprüche der Gäste zwingen jeden HORECA-Betrieb zur weiteren Rationalisierung und ständigen Verbesserung seiner Speisen. Immer häufiger wird zur fertigen Konserve gegriffen, nicht zuletzt wegen der damit verbundenen Dienstleistung für ein vielseitiges Angebot.</p>
    <p>Es ist daher nicht verwunderlich, dass aufgrund des chronischen Personalmangels immer mehr Gaststätte, Hotels, Großküchen und der Top-Party-Service den Wert und den Vorteil der rationell hergestellten Konserven erkennen.</p>
  </div>
</section>

<section class="products" style="height:644px">
  <h2 class="abs pill" style="top:0">Empfehlungen</h2>
  <div class="abs product-card" style="left:107px;top:133px">
    <div class="abs product-shot" role="img" aria-label="Konservendose Kartoffelsuppe"></div>
    <div class="product-name">Kartoffelsuppen-Terrine 1/4</div><div class="product-price">1,82 €</div><div class="product-note">inkl. MwSt. zzgl. Versandkosten</div>
    <div class="qty"><span class="step">-</span><span class="count">3</span><span class="step">+</span></div>
    <div class="add-cart"><svg width="16" height="16" viewBox="0 0 24 24" fill="none" stroke="#fff" stroke-width="2"><path d="M2 3h3l2.5 12h11L21 7H6"/><circle cx="9" cy="19.5" r="1.5"/><circle cx="17" cy="19.5" r="1.5"/></svg>In den Warenkorb</div>
  </div>
  <div class="abs product-card" style="left:461px;top:133px">
    <div class="abs product-shot" role="img" aria-label="Konservendose Hühnersuppe" style="background:linear-gradient(180deg,#d0d0d0,#c43a33 25%,#f2efe8 45%,#e07a3a 80%,#c0c0c0)"></div>
    <div class="product-name">Kartoffelsuppen-Terrine 1/4</div><div class="product-price">1,82 €</div><div class="product-note">inkl. MwSt. zzgl. Versandkosten</div>
    <div class="qty"><span class="step">-</span><span class="count">1</span><span class="step">+</span></div>
    <div class="add-cart"><svg width="16" height="16" viewBox="0 0 24 24" fill="none" stroke="#fff" stroke-width="2"><path d="M2 3h3l2.5 12h11L21 7H6"/><circle cx="9" cy="19.5" r="1.5"/><circle cx="17" cy="19.5" r="1.5"/></svg>In den Warenkorb</div>
  </div>
  <div class="abs product-card" style="left:814px;top:133px">
    <div class="abs product-shot" role="img" aria-label="Konservendose Hühnersuppe dunkel" style="background:linear-gradient(180deg,#b0b0b0,#8c1212 25%,#5a1010 60%,#3a0c0c 90%)"></div>
    <div class="product-name">Kartoffelsuppen-Terrine 1/4</div><div class="product-price">1,82 €</div><div class="product-note">inkl. MwSt. zzgl. Versandkosten</div>
    <div class="qty"><span class="step">-</span><span class="count">1</span><span class="step">+</span></div>
    <div class="add-cart"><svg width="16" height="16" viewBox="0 0 24 24" fill="none" stroke="#fff" stroke-width="2"><path d="M2 3h3l2.5 12h11L21 7H6"/><circle cx="9" cy="19.5" r="1.5"/><circle cx="17" cy="19.5" r="1.5"/></svg>In den Warenkorb</div>
  </div>
  <div class="abs slider-nav" style="top:522px">
    <span class="prev"><svg width="30" height="14" viewBox="0 0 30 14" fill="none" stroke="#999" stroke-width="1.6"><path d="M29 7H2M8 1L2 7l6 6"/></svg></span>
    <span class="next"><svg width="30" height="14" viewBox="0 0 30 14" fill="none" stroke="#fff" stroke-width="1.6"><path d="M1 7h27M22 1l6 6-6 6"/></svg></span>
  </div>
</section>

<section class="reviews">
  <div class="abs quote-mark">“</div>
  <h2>REZENSIONEN</h2>
  <p class="lead">Was unsere Kunden sagen</p>
  <div class="abs review-product" role="img" aria-label="Konservendose Hühnerbouillon"></div>
  <p class="review-text">Eine vorzügliche Bouillon, die auch und gerade als "Tassenportion" ausgezeichnet schmeckt. Seit 1975 genieße ich diese Brühe (nicht nur an kühlen Tagen) und war sehr enttäuscht, dass ich sie in unserer Region im Handel nicht mehr bekam.Aber hier : PR...</p>
  <p class="review-meta" style="top:370px"><b>Autor</b><br>Jonas Feldberg</p>
  <p class="review-meta" style="top:442px"><b>Artikel</b><br>Hühnerbouillon doppelt, 1 Kg (für 25 Ltr.)</p>
  <div class="abs dots"><span></span><span></span></div>
</section>

<footer class="site-footer">
  <div class="abs footer-brand"><span class="brand-name">kornhaus</span><span class="brand-sub">Foodservice</span></div>
  <h3 class="abs news-title">Abonnieren Sie unseren Newsletter</h3>
  <div class="abs news-form"><span class="news-input">E-Mail-Adresse</span><span class="news-btn">Abonnieren</span></div>

  <div class="abs foot-col" style="left:107px">
    <h3>BETREIBER DER WEBSITE</h3>
    <p>Brandmeier &amp; Co. GmbH &amp; Co. KG<br>Lindenallee 12 – 18<br>40723 Musterstadt, Deutschland</p>
    <p style="margin-top:18px"><span class="u">Telefon:</span>+49-(0)-2104-88320<br><span class="u">E-Mail:</span>info@kornhaus-suppen.de</p>
  </div>
  <div class="abs foot-col" style="left:403px">
    <h3>EINTRAGUNGEN</h3>
    <p>Register-Gericht Musterstadt HRA 20417<br>Register-Gericht Musterstadt HRB 38826</p>
    <p style="margin-top:18px">USt-IdNr.: DE 294817306</p>
  </div>
  <div class="abs foot-col" style="left:764px">
    <h3>INFORMATIONEN</h3>
    <p>Impressum<br>Haftungsausschluss<br>Datenschutzerklärung<br>Widerrufsbelehrung<br>AGB<br>Online-Streitbeilegung</p>
  </div>
  <svg class="abs to-top" width="22" height="24" viewBox="0 0 22 24" fill="none" stroke="#222" stroke-width="2"><path d="M11 23V2M3 10l8-8 8 8"/></svg>

  <div class="abs legal">
    <span>Copyright 2020. Alle Rechte vorbehalten.</span>
    <div class="social"><span></span><span></span></div>
  </div>
</footer>

</body>
</html>
```